Property Investor needs business card

Hi, we need a business card/logo/email footer/letterhead for a small family property investment business (based in Australia), to just give things a bit more of a professional "look".
Saying that, the property manager is in his late 30s, and is a fun, interesting guy so it doesn't have to be too "corporate" and serious.
Going with eg an 8cmx4cm card size could also make it a bit more interesting. Colour-wise - am relaxed.
Also, the property isn't so much "residential" ie houses/apartments, more "commercial" ie factories, office buildings, shops - in case that helps?
Lastly, the business name is "KPR", so you could also try to do something with those letters.
Enjoy!
Industry/Entity Type
Investment

```html
<!DOCTYPE html>
<html lang="en">
<head>
<meta charset="utf-8">
<title>KPR Property Investments – Business Card</title>
<link rel="stylesheet" href="https://fonts.googleapis.com/css2?family=Noto+Sans+Mono:wght@400&display=swap">
<style>
  :root {
    --forest: #4b7540;
    --sand: #cec4ae;
    --ink: #3a0800;
    --mono: "Noto Sans Mono", monospace;
  }
  html, body {
    margin: 0;
    padding: 0;
    overflow: hidden;
    background: var(--sand);
  }
  .card {
    position: relative;
    width: 1200px;
    height: 1200px;
    background: var(--sand);
    overflow: hidden;
    font-family: var(--mono);
    color: var(--ink);
  }
  .card__header {
    position: absolute;
    left: 0;
    top: 0;
    width: 1200px;
    height: 600px;
    background: var(--forest);
  }
  .brand-panel {
    position: absolute;
    left: 86px;
    top: 190px;
    width: 1021px;
    height: 374px;
    background: var(--sand);
  }
  .brand-panel__strip {
    position: absolute;
    left: 23px;
    top: 257px;
    width: 998px;
    height: 91px;
    background: var(--forest);
  }
  .brand-name {
    position: absolute;
    left: 0;
    width: 100%;
    top: 14px;
    margin: 0;
    text-align: center;
    font-size: 232px;
    font-weight: 400;
    line-height: 1;
    color: var(--ink);
  }
  .brand-tagline {
    position: absolute;
    left: 0;
    width: 100%;
    top: 0;
    margin: 0;
    text-align: center;
    font-size: 72px;
    font-weight: 400;
    line-height: 91px;
    color: var(--ink);
  }
  .contact {
    position: absolute;
    left: 70px;
    top: 812px;
    margin: 0;
    padding: 0;
    list-style: none;
    font-size: 62px;
    line-height: 75px;
  }
  .base-rule {
    position: absolute;
    left: 0;
    top: 1140px;
    width: 1110px;
    height: 20px;
    background: var(--forest);
  }
</style>
</head>
<body>
  <main class="card">
    <header class="card__header">
      <div class="brand-panel">
        <h1 class="brand-name">KPR</h1>
        <div class="brand-panel__strip">
          <p class="brand-tagline">PROPERTY INVESTMENTS</p>
        </div>
      </div>
    </header>

    <ul class="contact">
      <li class="contact__item">Name:</li>
      <li class="contact__item">Number:</li>
      <li class="contact__item">E-mail:</li>
    </ul>

    <div class="base-rule"></div>
  </main>
</body>
</html>
```